RTA Capital Campaign PWRPT Design

Our school is going to do a fund-raising campaign. I want to design a pwrpt around the campaign and need a design template using some of the images and the content I have laid out.

```html
<!DOCTYPE html>
<html lang="en">
<head>
<meta charset="utf-8">
<title>RTA Capital Campaign Slides</title>
<link rel="stylesheet" href="https://fonts.googleapis.com/css2?family=Signika:wght@400;600&family=Libre+Baskerville:wght@700&family=Didact+Gothic&display=swap">
<style>
:root{
  --stage:#d4d4d4;
  --purple:#4b1f72;
  --purple-deep:#381358;
  --purple-soft:#5e2d88;
  --orange:#e8860c;
  --white:#ffffff;
  --ink:#2a2a2a;
  --muted:#6a6a6a;
  --photo-warm:#b79a84;
  --photo-cool:#8c93a6;
  --photo-green:#8fa27c;
}
*{margin:0;padding:0;box-sizing:border-box}
html,body{width:1200px;height:1146px;overflow:hidden;background:var(--stage)}
body{position:relative;font-family:"Didact Gothic",sans-serif;color:var(--ink)}
.slide{position:absolute;width:386px;height:217px;background:var(--white);overflow:hidden}
.slide .bg{position:absolute;left:0;top:0;width:386px;height:217px}
.abs{position:absolute}
.photo{position:absolute;box-shadow:3px 4px 8px rgba(0,0,0,.35)}
.brand{position:absolute;display:flex;align-items:center;gap:5px;font-family:"Signika",sans-serif;font-weight:600;font-size:7px;letter-spacing:.8px;color:var(--white);text-transform:uppercase}
.brand .dot{width:14px;height:14px;border-radius:50%;background:var(--white)}
.brand.dark{color:var(--purple)}
.brand.dark .dot{background:var(--purple)}
.serif-title{font-family:"Libre Baskerville",serif;font-weight:700;color:var(--white)}
.in-title{position:absolute;font-family:"Signika",sans-serif;font-weight:600;font-size:18px;color:var(--purple);white-space:nowrap}
.in-title .are{color:var(--orange)}
.lead{font-style:italic;font-size:10px;line-height:1.1}
.lead b{font-style:italic}
.scripture{font-size:6.4px;line-height:1.18;text-align:justify}
.ref{font-size:6.4px}
.link{font-size:6.4px;color:#2d6cdf;text-decoration:underline}
.on-purple{color:var(--white)}
.on-purple .link{color:#8fb4ff}
.phase{position:absolute;display:flex;flex-direction:column;align-items:center;gap:6px;font-family:"Signika",sans-serif;font-size:23px;color:var(--purple)}
.partner{position:absolute;font-family:"Signika",sans-serif;font-size:6px;font-weight:600;color:var(--purple);display:flex;align-items:center;gap:3px}
.partner i{display:block;width:8px;height:8px;background:var(--purple)}
</style>
</head>
<body>

<section class="slide" style="left:16px;top:16px;background:var(--purple)">
  <svg class="bg" viewBox="0 0 386 217" preserveAspectRatio="none"><path d="M140 217 C230 200 330 150 386 70 L386 0 L300 0 C360 30 250 120 140 217Z" fill="#fff"/></svg>
  <div class="photo" role="img" aria-label="Black and white photo of a teacher with young students in handprint shirts" style="left:80px;top:38px;width:300px;height:200px;border-radius:50% 45% 40% 55%;background:linear-gradient(135deg,#cfcfcf,#8d8d8d);box-shadow:none"></div>
  <div class="brand" style="left:14px;top:14px"><span class="dot"></span>Ridgeline Trinity Academy</div>
  <div class="abs serif-title" style="left:130px;top:150px;font-size:24px;text-shadow:1px 1px 3px rgba(0,0,0,.5)">ARE YOU <span style="color:var(--purple)">IN?</span></div>
</section>

<section class="slide" style="left:408px;top:16px">
  <div class="photo" role="img" aria-label="Photo of a teacher and smiling children in handprint t-shirts outside the school" style="left:0;top:0;width:386px;height:174px;background:linear-gradient(160deg,var(--photo-green),#a9a9ad 55%,var(--photo-warm));box-shadow:none"></div>
  <div class="brand" style="left:10px;top:10px"><span class="dot"></span>Ridgeline Trinity Academy</div>
  <div class="abs" style="left:0;top:174px;width:386px;height:43px;background:var(--purple)"></div>
  <div class="abs serif-title" style="left:0;top:180px;width:386px;text-align:center;font-size:26px">Are you IN?</div>
</section>

<section class="slide" style="left:801px;top:16px">
  <div class="phase" style="left:22px;top:52px">
    <svg width="40" height="48" viewBox="0 0 40 48"><path d="M20 47 C10 34 2 28 2 19 A18 18 0 0 1 38 19 C38 28 30 34 20 47Z" fill="var(--purple)"/><circle cx="20" cy="19" r="12" fill="#fff"/><path d="M16 20 a4 5 0 1 1 8 0 l-1 3 h-6Z M17 25h6 M17.5 27h5" stroke="var(--purple)" stroke-width="1.2" fill="none"/></svg>
    Phase 1
  </div>
  <div class="brand dark" style="left:141px;top:18px;font-size:5px"><span class="dot" style="width:10px;height:10px"></span>Ridgeline Trinity</div>
  <div class="abs" style="left:194px;top:38px;font-family:'Libre Baskerville',serif;font-size:6px;color:var(--purple-deep)">RTA Courtyard Building Addition</div>
  <div class="abs" role="img" aria-label="Floor plan of classrooms and a science lab around a central corridor" style="left:140px;top:50px;width:208px;height:130px;background:linear-gradient(90deg,#f5e9b0 60%,#b8e4c4 60%);border:1px solid #999"></div>
  <div class="partner" style="left:141px;top:192px"><i></i>CRESTLINE</div>
  <div class="partner" style="left:300px;top:192px"><i></i>Halvorsen</div>
</section>

<section class="slide" style="left:16px;top:241px">
  <div class="phase" style="left:20px;top:62px">
    <svg width="40" height="48" viewBox="0 0 40 48"><path d="M20 47 C10 34 2 28 2 19 A18 18 0 0 1 38 19 C38 28 30 34 20 47Z" fill="var(--purple)"/><circle cx="20" cy="19" r="12" fill="#fff"/><path d="M16 20 a4 5 0 1 1 8 0 l-1 3 h-6Z M17 25h6 M17.5 27h5" stroke="var(--purple)" stroke-width="1.2" fill="none"/></svg>
    Phase 2
  </div>
  <div class="abs" role="img" aria-label="Aerial site master plan with athletic fields and new buildings" style="left:108px;top:12px;width:258px;height:184px;background:linear-gradient(180deg,#c9c9c9 38%,#9fc48a 38%,#9fc48a 62%,#c9c9c9 62%)"></div>
  <div class="abs" style="left:108px;top:199px;font-size:4.5px;color:var(--muted)">RTA MASTER PLAN</div>
</section>

<section class="slide" style="left:408px;top:241px">
  <div class="abs" style="left:0;top:8px;width:386px;text-align:center;font-size:9.5px">"Our Future:  Serving Generations"</div>
  <div class="abs" style="left:0;top:51px;width:300px;height:98px;background:var(--purple);box-shadow:4px 6px 10px rgba(0,0,0,.3)"></div>
  <div class="abs" style="left:7px;top:58px;width:286px;height:84px;border:1px solid rgba(255,255,255,.7)"></div>
  <div class="abs" style="left:0;top:80px;width:300px;text-align:center;font-family:'Signika',sans-serif;font-weight:600;font-size:30px;color:var(--white);letter-spacing:1px">ARE YOU IN?</div>
  <div class="abs" style="left:40px;top:160px;width:220px;text-align:center;font-style:italic;font-size:10px;line-height:1.35;color:var(--muted)">EXPECT GREAT THINGS FROM GOD<br>ATTEMPT  GREAT THINGS FOR GOD</div>
</section>

<section class="slide" style="left:801px;top:241px">
  <svg class="bg" viewBox="0 0 386 217" preserveAspectRatio="none"><path d="M0 178 C90 172 130 72 180 60 C250 44 320 36 386 28 L386 217 L0 217Z" fill="var(--purple)"/></svg>
  <div class="in-title" style="left:108px;top:12px"><span class="are">Are you</span> IN (vested)</div>
  <div class="photo" role="img" aria-label="Photo of smiling basketball players in team jerseys" style="left:18px;top:42px;width:152px;height:118px;background:linear-gradient(150deg,#d8d2c4,var(--photo-cool))"></div>
  <div class="abs on-purple" style="left:190px;top:77px;width:185px">
    <div class="lead"><b style="font-style:normal;font-weight:600">invested</b> in the next generation</div>
    <div style="font-size:5.8px;line-height:1.15;margin-top:12px">Invest in your child's future<br>Invest in the next generation<br>Invest in our culture<br>Invest in the community</div>
    <div class="scripture" style="font-size:5.6px;margin-top:6px">"Remember this—a farmer who plants only a few seeds will get a small crop. But the one who plants generously will get a generous crop. You must each decide in your heart how much to give. And don't give reluctantly or in response to pressure. "For God loves a person who gives cheerfully." And God will generously provide all you need. Then you will always have everything you need and plenty left over to share with others."<br>2 Corinthians 9:6-8 NLT</div>
    <div class="link" style="font-size:5.6px">versehub.org/2co.9.6-8</div>
  </div>
</section>

<section class="slide" style="left:16px;top:466px">
  <svg class="bg" viewBox="0 0 386 217" preserveAspectRatio="none"><path d="M386 0 L386 217 L230 217 C165 200 148 130 155 80 C162 40 180 12 200 0Z" fill="var(--purple)"/></svg>
  <div class="in-title" style="left:185px;top:20px;color:var(--white)"><span class="are">Are you</span> IN (debted)</div>
  <div class="photo" role="img" aria-label="Photo of a smiling girl at a computer lab desk" style="left:14px;top:52px;width:140px;height:88px;background:linear-gradient(120deg,#8aa6b8,var(--photo-warm))"></div>
  <div class="abs on-purple" style="left:172px;top:48px;width:204px">
    <div class="lead" style="text-align:justify"><b>Indebted</b> to the belief that we get to choose the culture for our children.</div>
    <div class="scripture" style="margin-top:9px">"After all, who is Apollos? Who is Paul? We are only God's servants through whom you believed the Good News. Each of us did the work the Lord gave us. I planted the seed in your hearts, and Apollos watered it, but it was God who made it grow. It's not important who does the planting, or who does the watering. What's important is that God makes the seed grow. The one who plants and the one who waters work together with the same purpose. And both will be rewarded for their own hard work. For we are both God's workers. And you are God's field. You are God's building."<br>1 Corinthians 3:5-9 NLT</div>
    <div class="link">versehub.org/1co.3.5-9</div>
  </div>
</section>

<section class="slide" style="left:408px;top:466px">
  <div class="abs" style="left:252px;top:0;width:134px;height:206px;background:var(--purple)"></div>
  <div class="in-title" style="left:19px;top:38px"><span class="are">Are you</span> IN (fluentail)</div>
  <div class="photo" role="img" aria-label="Photo of two smiling teenage students" style="left:200px;top:38px;width:172px;height:152px;background:linear-gradient(140deg,#c9a074,#6f5a4c)"></div>
  <div class="abs" style="left:19px;top:64px;width:176px">
    <div class="lead"><b>influential</b> in your child's future and the next generation.</div>
    <div class="scripture" style="font-size:8.4px;line-height:1.05;margin-top:20px">"Because of God's grace to me, I have laid the foundation like an expert builder. Now others are building on it. But whoever is building on this foundation must be very careful."</div>
    <div class="ref" style="font-style:italic">1 Corinthians 3:10 NLT</div>
    <div class="link" style="font-size:8.4px">versehub.org/1co.3.10</div>
  </div>
</section>

<section class="slide" style="left:801px;top:466px">
  <div class="abs" style="left:279px;top:0;width:107px;height:217px;background:var(--purple)"></div>
  <div class="in-title" style="left:24px;top:22px"><span class="are">Are you</span> IN (tune)</div>
  <div class="photo" role="img" aria-label="Photo of a smiling young girl in a colorful classroom" style="left:188px;top:14px;width:172px;height:76px;background:linear-gradient(120deg,#d46a5a,#e6c15a 50%,#5c84c2)"></div>
  <div class="photo" role="img" aria-label="Photo of high school students working at classroom desks" style="left:188px;top:118px;width:172px;height:78px;background:linear-gradient(120deg,#b9ad9b,#7d8a78)"></div>
  <div class="abs" style="left:16px;top:68px;width:166px">
    <div class="lead" style="text-align:justify"><b>in tune</b> with the cultural and learning aspects of your child's future</div>
    <div class="scripture" style="font-size:8.4px;line-height:.95;margin-top:20px">Do not conform to the pattern <b>of this world</b>, but be transformed by the renewing <b>of</b> your mind. Then you will be able to test and approve what God's will is—his good, pleasing and perfect will.</div>
  </div>
</section>

<section class="slide" style="left:16px;top:690px">
  <div class="abs" style="left:0;top:46px;width:386px;height:140px;background:var(--purple)"></div>
  <div class="in-title" style="left:14px;top:16px"><span class="are">Are you</span> IN (volved)</div>
  <div class="photo" role="img" aria-label="Photo of a mother and her teenage son standing together" style="left:212px;top:34px;width:162px;height:160px;background:linear-gradient(140deg,#9a8c7a,#5f8fb0)"></div>
  <div class="abs on-purple" style="left:14px;top:56px;width:186px">
    <div class="lead" style="font-size:9px"><b>involved</b> in the future of this community and lives of future children</div>
    <div class="scripture" style="margin-top:8px">"You know the saying, 'Four months between planting and harvest.' But I say, wake up and look around. The fields are already ripe for harvest. The harvesters are paid good wages, and the fruit they harvest is people brought to eternal life. What joy awaits both the planter and the harvester alike! You know the saying, 'One plants and another harvests.' And it's true. I sent you to harvest where you didn't plant; others had already done the work, and now you will get to gather the harvest."<br>John 4:35-38 NLT</div>
    <div class="link">versehub.org/jhn.4.35-38</div>
  </div>
</section>

<section class="slide" style="left:408px;top:690px">
  <svg class="bg" viewBox="0 0 386 217" preserveAspectRatio="none"><path d="M0 145 C90 110 200 190 386 130 L386 217 L0 217Z" fill="var(--purple)"/></svg>
  <div class="in-title" style="left:14px;top:12px;font-size:20px"><span class="are">Are you</span> IN (cluded)</div>
  <div class="abs" style="left:15px;top:38px;font-size:7.5px">Give today , make a difference  for tomorrow.</div>
  <div class="photo" role="img" aria-label="Photo of students working together at classroom computers" style="left:192px;top:62px;width:168px;height:134px;background:linear-gradient(130deg,#8d9cb4,#b99a86)"></div>
</section>

<section class="slide" style="left:801px;top:690px">
  <div class="abs" style="left:0;top:81px;width:386px;height:70px;background:var(--purple)"></div>
  <div class="in-title" style="left:21px;top:18px"><span class="are">Are you</span> IN (vited)</div>
  <div class="abs" style="left:24px;top:48px;font-size:6px">You are <b>invited</b> to be part of a growing community</div>
  <div class="photo" role="img" aria-label="Photo of students performing a stage play in costume" style="left:73px;top:70px;width:216px;height:116px;background:linear-gradient(160deg,#2b2220,#6e5a44 60%,#b08a5a)"></div>
</section>

<section class="slide" style="left:408px;top:916px;background:linear-gradient(180deg,var(--purple-soft),var(--purple-deep))">
  <div class="abs" style="left:52px;top:42px;width:288px;height:81px;background:var(--purple);box-shadow:3px 6px 10px rgba(0,0,0,.35)"></div>
  <div class="abs" style="left:52px;top:50px;width:288px;text-align:center;font-family:'Signika',sans-serif;font-weight:600;font-size:24px;line-height:1.28;color:var(--white)">Are you IN<br><span style="color:var(--orange)">I'm IN</span></div>
  <div class="brand" style="left:158px;top:160px"><span class="dot"></span>Ridgeline Trinity Academy</div>
</section>

</body>
</html>
```